Silver Heron Construction Services

Create a business card for my business consulting company
Danielle Vesk, Founder and CEO
4816 Alder Brook Way, Ste 100
Denver, CO. 80451
303.782.4190 cell
dvesk@silverheronconst.example
www.silverheronconst.example

Target Market(s)

Private Equity and Construction Companies

Industry/Entity Type

Business / Sales Consulting

Contact Information for Business Card

Tag Line that says "Where The Road To Success Is Always Under Construction"

Requirements
Must have
• Logo on both sides of the card.
Nice to have
• Add tagline to the same side of the card as my name and contact info

```html
<!DOCTYPE html>
<html lang="en">
<head>
<meta charset="utf-8">
<title>Silver Heron Construction Services – Business Card</title>
<link href="https://fonts.googleapis.com/css2?family=Montserrat:wght@400;500;600&family=Oswald:wght@500&display=swap" rel="stylesheet">
<style>
  :root {
    --page-bg: #3a3a3a;
    --card-black: #1c1c1c;
    --card-white: #ffffff;
    --ink-dark: #111111;
    --ink-light: #f2f2f2;
    --ink-silver: #b5b5b5;
    --rule: #4a4a4a;
  }
  * { box-sizing: border-box; margin: 0; padding: 0; }
  html, body {
    width: 1200px; height: 1200px; overflow: hidden;
    background: var(--page-bg);
    font-family: "Montserrat", sans-serif;
  }
  .sheet {
    width: 1200px; height: 1200px;
    display: flex; flex-direction: column; align-items: center; justify-content: center;
    gap: 60px;
  }
  .card {
    width: 900px; height: 515px; border-radius: 34px; overflow: hidden;
    position: relative; box-shadow: 0 14px 30px rgba(0,0,0,.45);
  }

  /* Front */
  .card--front { background: var(--card-black); }
  .front__top {
    position: absolute; left: 0; top: 0; width: 100%; height: 210px;
    background: var(--card-white);
  }
  .front__rule { position: absolute; left: 0; width: 100%; }
  .front__rule--dark { top: 210px; height: 12px; background: var(--card-black); }
  .front__rule--light { top: 222px; height: 9px; background: var(--card-white); }
  .front__brand {
    position: absolute; left: 0; top: 0; width: 100%; height: 210px;
    display: flex; align-items: center; justify-content: center; gap: 16px;
  }
  .brand-mark { width: 26px; height: 26px; background: var(--ink-dark); flex: none; }
  .brand-name {
    font-weight: 600; font-size: 30px; letter-spacing: 1px;
    text-transform: uppercase; color: var(--ink-dark); line-height: 1.1;
    text-align: left;
  }
  .front__person {
    position: absolute; left: 60px; top: 360px; color: var(--ink-light);
  }
  .person__name { font-weight: 600; font-size: 30px; letter-spacing: 1px; text-transform: uppercase; }
  .person__title { font-weight: 400; font-size: 17px; letter-spacing: 1px; text-transform: uppercase; margin-top: 4px; }
  .front__divider {
    position: absolute; left: 420px; top: 280px; width: 1px; height: 190px; background: var(--rule);
  }
  .front__contact {
    position: absolute; left: 450px; top: 285px; list-style: none; color: var(--ink-light);
    font-size: 18px; line-height: 1.45;
  }
  .contact__item { display: flex; align-items: flex-start; gap: 12px; }
  .contact__icon { width: 18px; height: 18px; flex: none; margin-top: 4px; }

  /* Back */
  .card--back { background: var(--card-black); }
  .back__brand {
    position: absolute; left: 0; top: 120px; width: 100%;
    display: flex; align-items: center; justify-content: center; gap: 20px;
  }
  .back__brand .brand-mark { background: var(--ink-silver); width: 34px; height: 34px; }
  .back__brand .brand-name { color: var(--ink-silver); font-size: 40px; }
  .back__tagline {
    position: absolute; left: 0; bottom: 70px; width: 100%; text-align: center;
    font-family: "Oswald", sans-serif; font-weight: 500; font-size: 27px;
    letter-spacing: 1.2px; color: var(--ink-silver); text-transform: uppercase;
    white-space: nowrap;
  }
</style>
</head>
<body>
<main class="sheet">
  <section class="card card--front">
    <div class="front__top"></div>
    <div class="front__rule front__rule--dark"></div>
    <div class="front__rule front__rule--light"></div>
    <div class="front__brand">
      <span class="brand-mark"></span>
      <span class="brand-name">Silver Heron<br>Construction Services</span>
    </div>
    <div class="front__person">
      <p class="person__name">Danielle Vesk</p>
      <p class="person__title">Founder and CEO</p>
    </div>
    <div class="front__divider"></div>
    <ul class="front__contact">
      <li class="contact__item">
        <svg class="contact__icon" viewBox="0 0 18 18"><rect x="4" y="1" width="10" height="16" rx="2" fill="none" stroke="#f2f2f2" stroke-width="1.6"/><line x1="8" y1="14" x2="10" y2="14" stroke="#f2f2f2" stroke-width="1.6"/></svg>
        <span>303.782.4190</span>
      </li>
      <li class="contact__item">
        <svg class="contact__icon" viewBox="0 0 18 18"><rect x="1" y="3.5" width="16" height="11" fill="#f2f2f2"/><polyline points="1,3.5 9,10 17,3.5" fill="none" stroke="#1c1c1c" stroke-width="1.4"/></svg>
        <span>dvesk@silverheronconst.example</span>
      </li>
      <li class="contact__item">
        <svg class="contact__icon" viewBox="0 0 18 18"><circle cx="9" cy="9" r="7.5" fill="none" stroke="#f2f2f2" stroke-width="1.5"/><ellipse cx="9" cy="9" rx="3.2" ry="7.5" fill="none" stroke="#f2f2f2" stroke-width="1.3"/><line x1="1.5" y1="9" x2="16.5" y2="9" stroke="#f2f2f2" stroke-width="1.3"/></svg>
        <span>www.silverheronconst.example</span>
      </li>
      <li class="contact__item">
        <svg class="contact__icon" viewBox="0 0 18 18"><path d="M9 17 C4 11 3 9 3 7 a6 6 0 0 1 12 0 c0 2 -1 4 -6 10z" fill="none" stroke="#f2f2f2" stroke-width="1.6"/><circle cx="9" cy="7" r="2" fill="#f2f2f2"/></svg>
        <span>4816 Alder Brook Way, Ste 100<br>Denver, CO. 80451</span>
      </li>
    </ul>
  </section>

  <section class="card card--back">
    <div class="back__brand">
      <span class="brand-mark"></span>
      <span class="brand-name">Silver Heron<br>Construction Services</span>
    </div>
    <p class="back__tagline">Where The Road to Success Is Always Under Construction</p>
  </section>
</main>
</body>
</html>
```